Real Estate Listing Signs for standard Yard arms

I need real estate listing signs done, for the standard sized sign to be hung beneath a white yard arm. To match existing logo. Information to be included:
-Logo
-Business name
-Phone number
-Marden Fosk Tundra Circle & Marden Fosk realty logos (smaller print)

Colors to be Red and anywhere in the gray scale between black and white, or a combination of those.

Target Market(s)

Drive by visuals

Industry/Entity Type

Real Estate Agent

Colors

Designer to choose only greyscale colors for use in the design.

Requirements
Must have
• My Logo and business name in same/similar font to whats provided, the MF tundra circle logo (small on bottom or corner somewhere), My phone number, and a decent amount of red coloration on the sign.

```html
<!DOCTYPE html>
<html lang="en">
<head>
<meta charset="utf-8">
<title>Brannick Realty – For Sale Yard Sign</title>
<link rel="stylesheet" href="https://fonts.googleapis.com/css2?family=Open+Sans:wght@600;700;800&display=swap">
<style>
  :root {
    --canvas-bg: #f4f4f4;
    --board-white: #ffffff;
    --panel-grey: #e3e4e5;
    --ink-black: #0d0d0d;
    --brand-red: #ec2330;
    --brokerage-grey: #5a5a5c;
  }
  * { margin: 0; padding: 0; box-sizing: border-box; }
  html, body {
    width: 1113px;
    height: 1200px;
    overflow: hidden;
    background: var(--canvas-bg);
    font-family: "Open Sans", Arial, sans-serif;
  }
  .yard-sign {
    position: absolute;
    left: 106px;
    top: 58px;
    width: 900px;
    height: 1084px;
    background: var(--board-white);
  }
  .sign-panel {
    position: absolute;
    left: 51px;
    top: 51px;
    right: 51px;
    bottom: 51px;
    background: var(--panel-grey);
  }
  .headline {
    position: absolute;
    left: 0;
    right: 0;
    top: 70px;
    text-align: center;
    font-weight: 800;
    font-size: 112px;
    line-height: 1;
    letter-spacing: -1px;
    color: var(--ink-black);
  }
  .brand-mark {
    position: absolute;
    left: 50%;
    top: 250px;
    width: 190px;
    height: 190px;
    margin-left: -95px;
  }
  .business-name {
    position: absolute;
    left: 0;
    right: 0;
    top: 528px;
    text-align: center;
    font-weight: 700;
    font-size: 80px;
    line-height: 97px;
    color: var(--ink-black);
  }
  .phone-band {
    position: absolute;
    left: 0;
    right: 0;
    top: 768px;
    height: 148px;
    background: var(--brand-red);
    display: flex;
    align-items: center;
    justify-content: center;
  }
  .phone-number {
    font-weight: 700;
    font-size: 88px;
    line-height: 1;
    color: var(--board-white);
    letter-spacing: 1px;
  }
  .brokerage-name {
    position: absolute;
    left: 0;
    right: 0;
    top: 944px;
    text-align: center;
    font-weight: 600;
    font-size: 34px;
    line-height: 1;
    color: var(--brokerage-grey);
  }
</style>
</head>
<body>
  <main class="yard-sign">
    <div class="sign-panel"></div>
    <h1 class="headline">FOR SALE</h1>
    <svg class="brand-mark" viewBox="0 0 190 190" aria-hidden="true">
      <rect x="0" y="0" width="190" height="190" fill="var(--brand-red)"/>
    </svg>
    <p class="business-name">BRANNICK<br>REALTY</p>
    <div class="phone-band">
      <span class="phone-number">555-301-0199</span>
    </div>
    <p class="brokerage-name">MF tundra circle</p>
  </main>
</body>
</html>
```